Tidecrest NZ Brand, Revenue, Promotions & Events

I need an innovative business card that pops my brand. I like the colours against darker gradients and i'm not afraid to be bold.

I run my own Business, Brand, Event & Promotion company. I specialise in breathing life into businesses and adding atmosphere to promotions and events. I am concept based lady that likes to test the boundaries and create stand out campaigns that connect with the consumer.

I have 12 years business experience in a realm of interesting fields form 11 years in coordinating international music festivals & promotions, 6 years in radio with 8 radio awards including a NZ radio award for best sales team in NZ and was the national brand and sales manager for New Zealands 1st indoor entertainment mall. With 10 years of experience in advertising sales, I have an eye for creating revenue streams for businesses and thrive on implementing campaigns that compliment those streams.

I love sayings like "Do what you love, love what you do" and believe that you can achieve anything you want.

I have been fortunate in my career that my connections have carried me without needing to promote my business however it is important that I start to do so.

Target Market(s)

Decision makers 25 to 54

Contact Information for Business Card

Petra Ollingham
Director
p. 022 587 3091
e. petra@tidecrest.nz
www.tidecrest.nz

FB, IG and Linkedin logo

Font styles to use
Sans Serif

Colors

Designer to choose colors to be used in the design.

Requirements
Must have
• Petra Ollingham
• Director
• p. 022 587 3091
• e. petra@tidecrest.nz
• www.tidecrest.nz
• FB, IG and Linkedin logo
Nice to have
• I am looking for a business card with character, that leaves my presence with my customer and makes them remember my brand & optimistic personality when i walk out the door.

```html
<!DOCTYPE html>
<html lang="en">
<head>
<meta charset="utf-8">
<title>Tidecrest NZ — Business Card</title>
<link href="https://fonts.googleapis.com/css2?family=Montserrat:wght@500;600;700&family=Arimo:wght@400&display=swap" rel="stylesheet">
<style>
  :root {
    --front-blue: #0280b4;
    --brand-blue: #1ea9e1;
    --ink: #3c3c3c;
    --slate: #555a60;
    --faint: #ededed;
    --page: #ffffff;
    --card-edge: #2a2a2a;
    --social-a: #e4405f;
    --social-b: #3b5998;
    --social-c: #1b8fd0;
  }
  * { margin: 0; padding: 0; box-sizing: border-box; }
  html, body { width: 1200px; height: 1200px; overflow: hidden; background: var(--page); }
  .canvas { position: relative; width: 1200px; height: 1200px; border: 1px solid #222; }
  .card {
    position: absolute; left: 240px; width: 720px; height: 440px;
    border: 1px solid var(--card-edge);
    box-shadow: 8px 8px 10px rgba(0,0,0,0.18);
    overflow: hidden;
  }
  .card--front { top: 135px; background: var(--front-blue); }
  .card--back { top: 624px; background: var(--page); }

  .wordmark {
    position: absolute; font-family: "Montserrat", sans-serif; font-weight: 600;
    letter-spacing: 3px; white-space: nowrap; line-height: 1;
  }
  .card--front .wordmark { left: 0; width: 100%; text-align: center; top: 176px; font-size: 58px; color: var(--page); }
  .card--back .wordmark { left: 48px; top: 283px; font-size: 48px; color: var(--brand-blue); top: 96px; }

  .tagline {
    position: absolute; font-family: "Arimo", sans-serif; white-space: nowrap; line-height: 1;
  }
  .card--front .tagline { left: 0; width: 100%; text-align: center; top: 247px; font-size: 25px; color: var(--page); }
  .card--back .tagline { left: 48px; top: 146px; font-size: 20.5px; color: var(--slate); }

  .faint-disc { position: absolute; left: 320px; top: 170px; width: 380px; height: 380px; border-radius: 50%; background: var(--faint); opacity: 0.7; }

  .person { position: absolute; left: 48px; top: 198px; font-family: "Montserrat", sans-serif; }
  .person__name { font-size: 28px; font-weight: 700; color: var(--brand-blue); line-height: 1; }
  .person__role { margin-top: 10px; font-size: 22px; font-weight: 500; color: var(--ink); line-height: 1; }

  .contact { position: absolute; left: 48px; top: 315px; font-family: "Montserrat", sans-serif; font-weight: 700; font-size: 19px; list-style: none; }
  .contact__item { display: flex; align-items: center; height: 30px; color: var(--ink); }
  .contact__icon { width: 26px; height: 22px; margin-right: 10px; display: block; }
  .contact__item--web { color: var(--brand-blue); }
  .contact__w { width: 26px; margin-right: 10px; color: var(--brand-blue); font-size: 20px; }

  .social { position: absolute; left: 524px; top: 370px; display: flex; gap: 10px; }
  .social__tile { width: 33px; height: 33px; border-radius: 3px; }
  .social__tile--one { background: var(--social-a); border-radius: 8px; }
  .social__tile--two { background: var(--social-b); }
  .social__tile--three { background: var(--social-c); }
</style>
</head>
<body>
<main class="canvas">
  <section class="card card--front" aria-label="Card front">
    <h1 class="wordmark">TIDECREST NZ</h1>
    <p class="tagline">BRAND | REVENUE | EVENTS &amp; PROMOTIONS</p>
  </section>

  <section class="card card--back" aria-label="Card back">
    <div class="faint-disc" aria-hidden="true"></div>
    <h2 class="wordmark">TIDECREST NZ</h2>
    <p class="tagline">BRAND | REVENUE | EVENTS &amp; PROMOTIONS</p>

    <div class="person">
      <p class="person__name">Petra Ollingham</p>
      <p class="person__role">Director</p>
    </div>

    <ul class="contact">
      <li class="contact__item">
        <svg class="contact__icon" viewBox="0 0 26 26" aria-hidden="true">
          <rect x="7" y="2" width="13" height="22" rx="3" fill="none" stroke="var(--brand-blue)" stroke-width="2.4"/>
          <circle cx="13.5" cy="20" r="1.3" fill="var(--brand-blue)"/>
        </svg>022 587 3091
      </li>
      <li class="contact__item">
        <svg class="contact__icon" viewBox="0 0 26 20" aria-hidden="true">
          <rect x="2" y="3" width="22" height="15" fill="none" stroke="var(--brand-blue)" stroke-width="2"/>
          <path d="M2 3 L13 11 L24 3 M2 18 L10 9 M24 18 L16 9" fill="none" stroke="var(--brand-blue)" stroke-width="2"/>
        </svg>petra@tidecrest.nz
      </li>
      <li class="contact__item contact__item--web">
        <span class="contact__w">W</span>www.tidecrest.nz
      </li>
    </ul>

    <div class="social">
      <span class="social__tile social__tile--one" role="img" aria-label="Social profile"></span>
      <span class="social__tile social__tile--two" role="img" aria-label="Social profile"></span>
      <span class="social__tile social__tile--three" role="img" aria-label="Professional network profile"></span>
    </div>
  </section>
</main>
</body>
</html>
```